Website Redesign for Technology Focused Investment Bank

We need a website redesign for a technology and digital media focused investment banking firm. Think modern and forward thinking yet stable and smart. We provide mergers and acquisitions advisory services to our clients. Our target market are CEO's and CFO's (senior executives) that run and operate technology firms.

Larkstone Capital Partners - www.larkstonecapitalpartners.example

We are headquartered in Los Angeles, CA. Please do NOT use the Pemberly marker for anything.

We have the content and can update the photos as well.

We are looking for a "template" website we can update and edit with ease.

A competitive firm's website is: www.brackenhale.example Not sure I like it but I want it to look way better then this one.

Looking for a more modern version. Not too stuffy and conservative, please. Elegant, smart, updated and progressive/modern.
Updates

Color preferences:  Blue's including matching logo color. Grey's. You can add other colors if it flows well and looks clean and nice.

Menu:  Drop Down

Open to platform...please use one that most people can use, is reasonably priced if I need to buy it, and easy to update monthly and sometimes weekly.

Please use this website as a good example of what we are looking for (or similar version of it): www.quelmora.example

Thanks!
Derek P.

We are reviewing all submissions and will select one this week. Thank you everyone for your outstanding and creative designs you have sent us. We really appreciate it.

Thanks for everyone's hard work and creative input into our website design. We really appreciate it!

Target Market(s)

CEO's and CFO's, Entrepreneurs and Board Members of Technology Companies.

Industry/Entity Type

Investment

Font styles to use
Sans Serif

Colors
33a6d7
0492cd
0555a3
3176b5
85abd2
333333
5c5c5c
757575

Requirements
Must have
• Links to social media including plain circle, plain circle, plain circle, plain circle, etc.

Must try to match logo color
Should not have
• No conservative, old looking colors or background. For example, no green marble look.

```html
<!DOCTYPE html>
<html lang="en">
<head>
<meta charset="utf-8">
<title>Larkstone Capital Partners</title>
<link href="https://fonts.googleapis.com/css2?family=Open+Sans:wght@400;600;700&family=Source+Sans+3:wght@400;600&display=swap" rel="stylesheet">
<style>
:root{
  --blue:#0555a3;
  --blue-light:#3176b5;
  --orange:#e8681f;
  --ink:#333333;
  --text:#757575;
  --mid:#5c5c5c;
  --rule:#d6d6d6;
  --page:#f4f4f4;
  --bar:#2b2b2b;
  --footer:#464646;
  --footer-dark:#333333;
}
*{margin:0;padding:0;box-sizing:border-box}
html,body{width:899px;height:1200px;overflow:hidden}
body{position:relative;background:var(--page);font-family:"Open Sans",sans-serif;color:var(--text);font-size:8.6px;line-height:1.45}
.abs{position:absolute}
.topbar{left:0;top:0;width:899px;height:19px;background:var(--bar)}
.search{left:473px;top:2px;width:161px;height:15px;background:#4a4a4a;border-radius:2px;color:#aaa;font-size:7.5px;padding:2px 6px}
.search svg{position:absolute;right:5px;top:3px}
.toplinks{right:118px;top:3px;color:#fff;font-size:7.5px}
.toplinks span{margin:0 4px;color:#bbb}
.header{left:0;top:19px;width:899px;height:68px;background:#fff;border-bottom:1px solid #ddd}
.brand{left:117px;top:12px;display:flex;align-items:center;gap:10px}
.brand-mark{width:40px;height:40px;border-radius:50%;background:var(--blue-light)}
.brand-name{font-family:"Source Sans 3",sans-serif;font-weight:600;color:var(--blue);font-size:17px;line-height:1.1;width:150px}
.nav{right:119px;top:41px;font-size:8.8px;color:var(--mid)}
.nav a{color:var(--mid);text-decoration:none}
.nav .on{color:var(--orange)}
.nav span{margin:0 4px;color:#999}
.hero{left:0;top:87px;width:899px;height:365px;background:linear-gradient(135deg,#cfd6de 0%,#8d9aa8 35%,#c7a98f 55%,#7d8a99 75%,#d7dde3 100%)}
.caption{left:154px;top:39px;width:576px;height:60px;background:rgba(90,98,110,.6);color:#fff;font-family:"Source Sans 3",sans-serif;font-weight:600;font-size:14.5px;line-height:1.3;text-align:center;padding:10px 14px}
.dots{left:404px;top:343px;width:90px;height:22px;background:#fff;border-radius:4px 4px 0 0;display:flex;justify-content:center;align-items:center;gap:5px}
.dots i{width:8px;height:8px;border-radius:50%;background:#aaa}
.dots i.on{background:var(--orange)}
h2{font-family:"Source Sans 3",sans-serif;font-weight:400;color:var(--ink);font-size:16px}
.sectors-title{left:0;top:474px;width:899px;text-align:center}
.sector{top:508px;width:203px}
.sector h3{font-family:"Source Sans 3",sans-serif;font-weight:400;font-size:11.5px;color:var(--text);padding-bottom:5px;border-bottom:1px solid var(--rule);position:relative}
.sector h3::after{content:"";position:absolute;left:0;bottom:-1px;width:104px;height:1px;background:#999}
.sector.on h3{color:var(--orange)}
.sector .body{display:flex;gap:8px;margin-top:12px}
.sector p{font-size:8.4px;line-height:1.33}
.dotline{left:117px;width:663px;border-top:1px dotted #c8c8c8}
.why{left:117px;top:626px;width:436px}
.why p{margin-top:8px}
.why p:first-of-type{margin-top:11px}
.why a{color:var(--orange)}
.btn{display:inline-block;background:var(--orange);color:#fff;font-size:8.5px;font-weight:600;width:76px;height:22px;line-height:22px;text-align:center;border-radius:2px}
.services{left:588px;top:626px;width:200px}
.services ul{list-style:none;margin-top:10px}
.services li{color:var(--text);font-size:8.6px;height:20px;padding-left:12px;position:relative}
.services li::before{content:"›";position:absolute;left:0;top:-2px;font-size:11px;color:#999}
.partners{left:117px;top:858px;width:663px;height:40px;display:flex;align-items:center;justify-content:space-between}
.partner{font-family:"Source Sans 3",sans-serif;font-weight:600;font-size:15px;color:#555}
.news{left:117px;top:938px;width:436px}
.news-head{display:flex;justify-content:space-between;align-items:flex-end;border-bottom:1px solid var(--rule);padding-bottom:5px;position:relative}
.news-head::after{content:"";position:absolute;left:0;bottom:-1px;width:130px;height:1px;background:#999}
.pager{font-size:7.6px;color:var(--ink)}
.posts{display:flex;gap:26px;margin-top:20px}
.post{display:flex;gap:10px;width:205px}
.post h4{font-family:"Source Sans 3",sans-serif;font-weight:400;font-size:10.5px;line-height:1.45;color:var(--orange)}
.post.plain h4{color:var(--mid)}
.post time{display:block;margin-top:12px;font-size:8px;color:var(--mid)}
.newsletter{left:587px;top:938px;width:193px}
.newsletter h2{border-bottom:1px solid var(--rule);padding-bottom:5px;position:relative}
.newsletter h2::after{content:"";position:absolute;left:0;bottom:-1px;width:130px;height:1px;background:#999}
.email{margin-top:22px;height:20px;border:1px solid #ddd;background:#fff;font-style:italic;color:#999;font-size:7.2px;padding:4px 7px}
.signup{margin-top:9px;width:67px;height:17px;border:1px solid #ccc;background:linear-gradient(#fff,#e8e8e8);color:var(--orange);font-weight:700;font-size:7.6px;text-align:center;line-height:15px;border-radius:2px}
.tweets{left:0;top:1065px;width:899px;height:97px;background:var(--footer);color:#fff;text-align:center}
.tweets h2{color:#fff;margin-top:12px;display:flex;justify-content:center;align-items:center;gap:8px}
.tweets h2 i{width:16px;height:16px;border-radius:50%;background:#fff;display:inline-block}
.tweet{margin-top:7px;font-size:9px;color:#ddd}
.tweet b{font-family:"Source Sans 3",sans-serif;font-weight:600;font-size:12.5px;color:#fff}
.tweet a{color:var(--orange)}
.summary{margin-top:5px;font-size:8px;font-weight:600;text-decoration:underline}
.bottombar{left:0;top:1162px;width:899px;height:38px;background:var(--footer-dark)}
.copy{left:117px;top:13px;font-size:8px;color:#aaa}
.copy a{color:var(--blue-light)}
.social{right:118px;top:10px;display:flex;gap:8px}
.social i{width:16px;height:16px;border-radius:50%;background:#fff;display:block}
</style>
</head>
<body>
<div class="abs topbar">
  <div class="abs search">Search...
    <svg width="9" height="9" viewBox="0 0 10 10"><circle cx="4" cy="4" r="3" fill="none" stroke="#bbb" stroke-width="1.4"/><line x1="6.3" y1="6.3" x2="9.3" y2="9.3" stroke="#bbb" stroke-width="1.5"/></svg>
  </div>
  <div class="abs toplinks">About Us<span>|</span>News+Blog<span>|</span>Contact Us</div>
</div>

<header class="abs header">
  <div class="abs brand"><div class="brand-mark"></div><div class="brand-name">Larkstone Capital Partners</div></div>
  <nav class="abs nav"><a class="on">Home</a><span>|</span><a>Services</a><span>|</span><a>Transactions</a><span>|</span><a>Research</a><span>|</span><a>Private Equity</a><span>|</span><a>Recommendations</a><span>|</span><a>About the Founder</a><span>|</span><a>Careers</a></nav>
</header>

<section class="abs hero" role="img" aria-label="Photo of two business people in suits shaking hands">
  <div class="abs caption">Lorem ipsum dolor sit amet, consectetur adipiscing elit. Sed hendrerit lorem id nunc condimentum vulputate id eget risus. Duis facilisis, augue id posuere convallis</div>
  <div class="abs dots"><i></i><i class="on"></i><i></i><i></i><i></i></div>
</section>

<h2 class="abs sectors-title">Industry Sectors We Cover</h2>

<div class="abs sector on" style="left:117px">
  <h3>Software</h3>
  <div class="body">
    <svg width="50" height="34" viewBox="0 0 50 34"><rect x="6" y="2" width="38" height="24" rx="2" fill="none" stroke="#555" stroke-width="2"/><rect x="1" y="27" width="48" height="4" rx="1" fill="#555"/><circle cx="17" cy="14" r="5" fill="var(--orange)"/><rect x="25" y="11" width="13" height="2" fill="#555"/><rect x="25" y="16" width="9" height="2" fill="#555"/></svg>
    <p>Our professionals are able to assist with complex strategic and financial M&amp;A transactions within the software industry.</p>
  </div>
</div>
<div class="abs sector" style="left:349px">
  <h3>IT Services</h3>
  <div class="body">
    <svg width="50" height="34" viewBox="0 0 50 34"><rect x="6" y="2" width="38" height="24" rx="2" fill="none" stroke="#555" stroke-width="2"/><rect x="1" y="27" width="48" height="4" rx="1" fill="#555"/><circle cx="22" cy="12" r="4.5" fill="none" stroke="#555" stroke-width="2.5"/><circle cx="30" cy="18" r="3" fill="none" stroke="#555" stroke-width="2"/></svg>
    <p>We provide investment banking and M&amp;A advisory services to some of the largest IT Services firms across the globe.</p>
  </div>
</div>
<div class="abs sector" style="left:587px">
  <h3>Internet and Digital Media</h3>
  <div class="body">
    <svg width="42" height="34" viewBox="0 0 42 34"><rect x="12" y="2" width="26" height="20" rx="2" fill="none" stroke="#555" stroke-width="2"/><rect x="1" y="12" width="12" height="20" rx="2" fill="none" stroke="#555" stroke-width="2"/><rect x="20" y="18" width="20" height="14" rx="2" fill="#fff" stroke="#555" stroke-width="2"/></svg>
    <p>We provide investment banking and M&amp;A advisory services to some of the largest Internet and Digital Media firms across the globe.</p>
  </div>
</div>

<div class="abs dotline" style="top:607px"></div>

<section class="abs why">
  <h2>Why Us?</h2>
  <p>We are an independent investment bank and M&amp;A advisory firm focused exclusively on the global Technology and Digital Media sectors. Specifically, we execute mergers and acquisitions for the <a>Software</a>, <a>IT Services</a>, <a>Internet and Digital Media</a> industry sectors.</p>
  <p>Our professionals have completed over $20 billion in transactions to date and have experience in investment banking, private equity and capital markets from leading firms. We are experts in complex M&amp;A transactions of most shapes and sizes and have deep industry expertise.</p>
  <p>We advise companies, entrepreneurs, majority shareholders and leading institutions on complex strategic and financial transactions including mergers, acquisitions, divestitures, asset sales, spin-offs and related corporate finance issues that create and increase shareholder value.</p>
</section>
<div class="abs btn" style="left:117px;top:802px">Read More</div>

<section class="abs services">
  <h2>Services Provided</h2>
  <ul>
    <li>Buy-Side Mergers and Acquisitions</li>
    <li>Sell-Side Mergers and Acquisitions</li>
    <li>Recapitalizations and Restructuring's</li>
    <li>Equity and Debt Buyout Financing (Advisory)</li>
    <li>Spin-Offs and Asset Sales</li>
    <li>Strategic and Corporate Finance Advisory</li>
    <li>Fairness Opinions and Valuations</li>
  </ul>
</section>
<div class="abs btn" style="left:588px;top:802px">Read More</div>

<div class="abs dotline" style="top:846px"></div>

<div class="abs partners">
  <span class="partner">Kestova</span>
  <span class="partner">Alderwyn Group</span>
  <span class="partner">Brightmesh</span>
  <span class="partner">Tarnfield Equity</span>
  <svg width="14" height="24" viewBox="0 0 14 24"><polyline points="2,2 12,12 2,22" fill="none" stroke="#bbb" stroke-width="1.5"/></svg>
</div>

<section class="abs news">
  <div class="news-head"><h2 style="font-size:13px">Technology and Digital Media Mergers News and Blog</h2><span class="pager">&lt;&lt; Previous &nbsp;|&nbsp; Next &gt;&gt;</span></div>
  <div class="posts">
    <div class="post">
      <svg width="28" height="24" viewBox="0 0 28 24"><rect x="1" y="1" width="26" height="22" fill="none" stroke="#bbb" stroke-width="1.5"/><rect x="5" y="6" width="8" height="6" fill="#ccc"/><rect x="15" y="6" width="8" height="1.5" fill="#ccc"/><rect x="15" y="10" width="8" height="1.5" fill="#ccc"/><rect x="5" y="15" width="18" height="1.5" fill="#ccc"/></svg>
      <div><h4>Technology Mergers on Upswing in Q1 2014</h4><time>Fri, Feb 14 2014 - 12:04 AM</time></div>
    </div>
    <div class="post plain">
      <svg width="28" height="24" viewBox="0 0 28 24"><rect x="1" y="1" width="26" height="22" fill="none" stroke="#bbb" stroke-width="1.5"/><rect x="5" y="6" width="8" height="6" fill="#ccc"/><rect x="15" y="6" width="8" height="1.5" fill="#ccc"/><rect x="15" y="10" width="8" height="1.5" fill="#ccc"/><rect x="5" y="15" width="18" height="1.5" fill="#ccc"/></svg>
      <div><h4>Dorian Vell will be a speaker at the Mobile Host Show - The Mobile...</h4><time>Thu, May 23 2013 - 5:44 PM</time></div>
    </div>
  </div>
</section>

<section class="abs newsletter">
  <h2 style="font-size:13px">Newsletter Sign Up</h2>
  <div class="email">Your Email Adress</div>
  <div class="signup">SIGN UP</div>
</section>

<section class="abs tweets">
  <h2><i></i>Tweets</h2>
  <p class="tweet"><b>Larkstone Capital @LarkstoneDeals</b> M&amp;A - Best Start to Year Since 2011 <a>lnk.example/k7Qa</a></p>
  <p class="summary">Show Summary</p>
</section>

<footer class="abs bottombar">
  <div class="abs copy">Copyright 2014 <a>Larkstone Capital Partners, LLC</a> . All Rights Reserved</div>
  <div class="abs social"><i></i><i></i><i></i><i></i></div>
</footer>
</body>
</html>
```